Business Card Design

our business is purchasing, rehabbing and flipping homes. Design a house in the palm of a hand. This card is for a new company based in Georgia. So we buy homes that have been foreclosed, short sales,abandond, old homes and vacant homes.
We help improve the communities that we work in. We would like to see designs that use a black background with green accent and other colors that blend and don't take away from the logo and other important information.

Industry/Entity Type

Business

Contact Information for Business Card

Hollow Pine Ventures
Turning Every Key Toward Home
2867 Ledgemoor Lane
Duluth GA 30096
Office: 678-555-0142
hollowpineventuresllc.example

```html
<!DOCTYPE html>
<html lang="en">
<head>
<meta charset="utf-8">
<title>Hollow Pine Ventures — Business Card</title>
<link href="https://fonts.googleapis.com/css2?family=Ubuntu:wght@400;500;700&family=Oswald:wght@400;500&display=swap" rel="stylesheet">
<style>
  :root {
    --card-black: #0d0d0d;
    --accent-green: #9ee02a;
    --text-white: #ffffff;
    --backdrop: #e4e4e2;
  }
  * { box-sizing: border-box; margin: 0; padding: 0; }
  html, body {
    width: 1200px;
    height: 849px;
    overflow: hidden;
    background: var(--backdrop);
  }
  .stage {
    width: 1200px;
    height: 849px;
    display: flex;
    align-items: center;
    justify-content: center;
  }
  .business-card {
    position: relative;
    width: 1000px;
    height: 571px;
    background: var(--card-black);
    color: var(--text-white);
    font-family: "Ubuntu", sans-serif;
    border-radius: 4px;
    box-shadow: 0 10px 30px rgba(0,0,0,0.25);
    overflow: hidden;
  }
  .brand {
    position: absolute;
    top: 130px;
    left: 0;
    right: 0;
    display: flex;
    flex-direction: column;
    align-items: center;
  }
  .brand-lockup {
    display: flex;
    align-items: center;
    gap: 22px;
  }
  .brand-dot {
    width: 46px;
    height: 46px;
    border-radius: 50%;
    background: var(--accent-green);
  }
  .brand-name {
    font-family: "Ubuntu", sans-serif;
    font-weight: 700;
    font-size: 68px;
    letter-spacing: 2px;
    text-transform: uppercase;
    color: var(--text-white);
    line-height: 1;
  }
  .tagline {
    margin-top: 22px;
    font-family: "Oswald", sans-serif;
    font-weight: 400;
    font-size: 27px;
    letter-spacing: 1.5px;
    text-transform: uppercase;
    color: var(--text-white);
  }
  .contact-row {
    position: absolute;
    top: 388px;
    left: 60px;
    right: 60px;
    display: flex;
    justify-content: space-between;
    font-size: 24px;
    font-weight: 400;
  }
  .contact-item {
    display: flex;
    align-items: center;
    gap: 12px;
  }
  .contact-icon {
    width: 22px;
    height: 22px;
    flex: none;
  }
  .web-band {
    position: absolute;
    top: 440px;
    left: 0;
    right: 0;
    height: 70px;
    background: var(--accent-green);
    display: flex;
    align-items: center;
    padding-left: 60px;
  }
  .web-address {
    font-family: "Ubuntu", sans-serif;
    font-weight: 700;
    font-size: 30px;
    letter-spacing: 1px;
    text-transform: uppercase;
    color: var(--card-black);
  }
</style>
</head>
<body>
  <main class="stage">
    <section class="business-card" aria-label="Hollow Pine Ventures business card">
      <div class="brand">
        <div class="brand-lockup">
          <span class="brand-dot" aria-hidden="true"></span>
          <h1 class="brand-name">Hollow Pine Ventures</h1>
        </div>
        <p class="tagline">Turning Every Key Toward Home</p>
      </div>

      <div class="contact-row">
        <p class="contact-item address">
          <svg class="contact-icon" viewBox="0 0 24 24" aria-hidden="true">
            <circle cx="12" cy="12" r="11" fill="#9ee02a"/>
            <path d="M12 5.5a4 4 0 0 0-4 4c0 3 4 8 4 8s4-5 4-8a4 4 0 0 0-4-4zm0 5.6a1.6 1.6 0 1 1 0-3.2 1.6 1.6 0 0 1 0 3.2z" fill="#0d0d0d"/>
          </svg>
          2867 Ledgemoor Lane Duluth GA 30096
        </p>
        <p class="contact-item phone">
          <svg class="contact-icon" viewBox="0 0 24 24" aria-hidden="true">
            <circle cx="12" cy="12" r="11" fill="#9ee02a"/>
            <path d="M8.6 6.5l1.8-.3 1 2.6-1.3 1a6.5 6.5 0 0 0 3.1 3.1l1-1.3 2.6 1-.3 1.8c-.1.6-.7 1-1.3 1A8.3 8.3 0 0 1 7.6 7.8c0-.6.4-1.2 1-1.3z" fill="#0d0d0d"/>
          </svg>
          Office: 678-555-0142
        </p>
      </div>

      <div class="web-band">
        <p class="web-address">hollowpineventuresllc.example</p>
      </div>
    </section>
  </main>
</body>
</html>
```